RV Parts Business for Sale

I am anonymously selling my RV replacements parts business. One post card will be displayed at various RV parks and rallies and is applicable to a 'general audience' The second post card is to entice existing RV vendors to add to their profits by buying my business. The viewers MUST NOT be able to identify the business name or product. This is only to spark enough interest for them to request more information via mail. The cards must be of high quality and sophistication, as to attract affluent interested parties. See attached concept files, but I am open to your professional expertise. The watermark on the first concept is too dark, but I don't have any way to manipulate it.

Industry/Entity Type

Business

```html
<!DOCTYPE html>
<html lang="en">
<head>
<meta charset="utf-8">
<title>RV Parts Business for Sale – Postcards</title>
<link href="https://fonts.googleapis.com/css2?family=Arimo:wght@400;500;700&family=Tenor+Sans&display=swap" rel="stylesheet">
<style>
  :root {
    --stage: #2b1a12;
    --sky-deep: #6e1a08;
    --sky-mid: #b8380c;
    --sky-glow: #e0701a;
    --band-orange: #ff7a12;
    --band-light: #ff9a1c;
    --strip-dark: #5a140a;
    --cream: #fff3c8;
    --gold: #ffc21a;
    --gold-deep: #c98a1a;
    --profit-red: #ff1a0a;
    --bullet-red: #b8100a;
    --ink: #111111;
    --flag-blue: #2a3aa8;
    --back-box: #ff8a12;
    --rv-dark: #2a1406;
    --rv-mid: #6a3a12;
    --rv-light: #c8923a;
    --rv-back-dark: #7a4a10;
    --rv-back-mid: #b8741a;
  }
  * { margin: 0; padding: 0; box-sizing: border-box; }
  html, body { width: 1200px; height: 1000px; overflow: hidden; background: var(--stage); }
  .canvas { position: relative; width: 1200px; height: 1000px; }

  /* Back card */
  .card-back {
    position: absolute; left: 450px; top: 418px; width: 708px; height: 544px;
    box-shadow: 0 6px 16px rgba(0,0,0,.5); overflow: hidden;
  }
  .card-back .scene {
    position: absolute; inset: 0;
    background: linear-gradient(180deg, #f7b23a 0%, #f29a1e 45%, #d9801a 70%, #f0a030 100%);
  }
  .card-back .rv-photo {
    position: absolute; left: 15px; top: 168px; width: 490px; height: 232px;
    border-radius: 30px 20px 8px 8px;
    background: linear-gradient(180deg, var(--rv-back-mid) 0%, var(--rv-back-dark) 55%, var(--rv-back-mid) 100%);
    opacity: .8;
  }
  .mail-panel {
    position: absolute; left: 340px; top: 167px; width: 368px; height: 290px;
    background: var(--back-box); opacity: .95;
    box-shadow: -2px 2px 8px rgba(0,0,0,.25);
  }
  .mail-panel .address {
    position: absolute; left: 73px; top: 110px;
    font: 700 14px/18px "Arimo", sans-serif; color: var(--ink);
  }

  /* Front card */
  .card-front {
    position: absolute; left: 35px; top: 30px; width: 710px; height: 543px;
    box-shadow: 0 8px 18px rgba(0,0,0,.6); overflow: hidden;
  }
  .card-front .scene {
    position: absolute; left: 0; top: 0; width: 710px; height: 405px;
    background:
      radial-gradient(ellipse at 70% 75%, var(--sky-glow) 0%, transparent 55%),
      linear-gradient(180deg, var(--sky-deep) 0%, var(--sky-mid) 45%, #c8581a 75%, #7a3210 100%);
  }
  .card-front .rv-photo {
    position: absolute; left: 0; top: 125px; width: 490px; height: 230px;
    border-radius: 0 40px 10px 10px;
    background: linear-gradient(180deg, var(--rv-light) 0%, var(--rv-mid) 35%, var(--rv-dark) 70%, var(--rv-mid) 100%);
  }
  .headline {
    position: absolute; left: 75px; top: 16px;
    font-family: "Tenor Sans", sans-serif; font-variant: small-caps; font-weight: 400;
    color: var(--cream); letter-spacing: 1px; white-space: nowrap;
    text-shadow: 0 1px 3px rgba(0,0,0,.6);
  }
  .headline .line1 { font-size: 30px; line-height: 46px; }
  .headline .us { color: var(--flag-blue); font-family: "Arimo", sans-serif; font-weight: 700; text-shadow: 0 0 2px #fff; }
  .headline .free { color: var(--gold); font-size: 44px; }
  .headline .free sup { font-size: 20px; }
  .headline .line2 { font-size: 28px; line-height: 34px; margin-left: 235px; }
  .big-free {
    position: absolute; right: 14px; top: 118px;
    font: 400 72px/1 "Arimo", sans-serif; color: var(--gold-deep);
  }
  .tagline-strip {
    position: absolute; left: 0; top: 372px; width: 710px; height: 33px;
    background: linear-gradient(180deg, rgba(60,14,6,.2), rgba(60,14,6,.75));
    text-align: center;
    font: 700 15px/33px "Arimo", sans-serif; color: var(--cream);
  }
  .tagline-strip em { font-style: normal; color: var(--gold); }
  .features {
    position: absolute; left: 0; top: 405px; width: 710px; height: 110px;
    background: linear-gradient(180deg, var(--band-orange), var(--band-light));
    display: grid; grid-template-columns: 370px 340px; padding: 4px 0 0 55px;
    list-style: none;
  }
  .features li {
    position: relative; padding-left: 25px; height: 26px;
    font: 500 15px/26px "Arimo", sans-serif; color: var(--ink);
  }
  .features li::before {
    content: ""; position: absolute; left: 0; top: 8px; width: 10px; height: 10px;
    background: var(--bullet-red); box-shadow: 1px 1px 0 #6a0804;
  }
  .features .profit { color: var(--profit-red); font-weight: 700; }
  .footnote {
    position: absolute; left: 0; top: 515px; width: 710px; height: 28px;
    background: var(--strip-dark); text-align: center;
    font: 400 13px/28px "Arimo", sans-serif; color: var(--gold);
  }
</style>
</head>
<body>
<div class="canvas">

  <section class="card-back">
    <div class="scene"></div>
    <div class="rv-photo" role="img" aria-label="Faded orange-toned photograph of a luxury motorhome parked on open desert flats"></div>
    <div class="mail-panel">
      <p class="address">For more information write to:<br>Vendor Inquiry 2140 Canyon View Dr.<br>Fort Collins, CO 80525</p>
    </div>
  </section>

  <section class="card-front">
    <div class="scene"></div>
    <div class="rv-photo" role="img" aria-label="Sunset-toned photograph of a luxury motorhome on a desert road under a red sky"></div>
    <h1 class="headline">
      <div class="line1">Travel the <span class="us">US</span> for <span class="free">FREE<sup>*</sup></span> while ...</div>
      <div class="line2">earning extra Money</div>
    </h1>
    <div class="big-free">FREE</div>
    <p class="tagline-strip">Supply replacement parts to the rapidly <em>EXPANDING</em> recreational travel industry</p>
    <ul class="features">
      <li>Extremely aggressive <span class="profit">PROFIT</span> margins</li>
      <li>Over 10 years in the industry</li>
      <li>Pick your own destination</li>
      <li>Attend RV Rallies and Shows</li>
      <li>Turn-Key operation</li>
      <li>Strictly confidential</li>
      <li>Nationally recognized name</li>
      <li>Offered at $387,000</li>
    </ul>
    <p class="footnote">*Expenses are paid by your company. Consult your Tax Professional for details</p>
  </section>

</div>
</body>
</html>
```